Modern brochure by Lawyers, for modern clients

It'sa "News" for their clients. Attached you can find the current News without design. It must be elegant but very attractive and modern. Their web site is http://www.montalbanyasociados.cl/ Their expertise is labor and employment practice area. It must be in editable format so that lawyers can write the news in a template with this corporate design.

Target Market(s)

Big Companies

Font styles to use
Sans Serif

Colors
0255a3
474747

Requirements
Nice to have
• Legal Pictures and only a little of yellow. One touch! It must be in editable format so that lawyers can write the news in a template with this corporate design.

```html
<!DOCTYPE html>
<html lang="es">
<head>
<meta charset="utf-8">
<title>Boletín laboral — Montalbán y Asociados</title>
<link href="https://fonts.googleapis.com/css2?family=Roboto:ital,wght@0,300;0,400;0,500;0,700;1,400;1,700&display=swap" rel="stylesheet">
<style>
:root{
  --backdrop:#5f666e;
  --paper:#ffffff;
  --brand-blue:#0255a3;
  --ink:#474747;
  --navy:#3a4c6b;
  --accent-yellow:#f0e020;
  --yellow-soft:#e8dc3c;
  --panel:#e4eaf3;
}
*{box-sizing:border-box;margin:0;padding:0}
html,body{width:1200px;height:905px;overflow:hidden}
body{background:var(--backdrop);font-family:'Roboto',sans-serif;color:var(--ink)}
.newsletter{position:absolute;left:289px;top:12px;width:622px;height:880px;background:var(--paper);overflow:hidden;box-shadow:0 6px 18px rgba(0,0,0,.35)}
.header-art{position:absolute;left:0;top:0}
.brand{position:absolute;display:flex;align-items:center;gap:10px}
.brand-mark{width:26px;height:26px;border-radius:50%;background:var(--navy);flex:none}
.brand-name{font-weight:300;color:var(--navy);letter-spacing:2px;text-transform:uppercase;line-height:1.05}
.header-brand{left:34px;top:54px}
.header-brand .brand-name{font-size:20px}
.issue-date{position:absolute;right:24px;top:112px;display:flex;align-items:center;gap:10px;color:var(--accent-yellow);font-size:12.5px;font-weight:300;line-height:1.25}
.issue-date svg{flex:none}
.letter{position:absolute;left:40px;right:40px;top:188px;font-size:11.6px;line-height:1.42}
.greeting{color:var(--brand-blue);font-weight:700;font-style:italic;margin-bottom:8px}
.letter p{text-indent:22px;margin-bottom:9px;text-align:left}
.letter .highlight{font-weight:700;font-style:italic;text-indent:22px}
.letter a{color:var(--brand-blue);font-weight:700;text-decoration:underline}
.letter .closing{margin-top:4px}
.signature{position:absolute;left:40px;top:510px;display:flex;align-items:center;gap:12px}
.portrait{width:52px;height:52px;border-radius:50%;border:3px solid var(--brand-blue);background:linear-gradient(160deg,#c9d3df,#6d7c92)}
.sig-name{color:var(--brand-blue);font-weight:700;font-style:italic;font-size:13px}
.sig-mail{display:flex;align-items:center;gap:6px;font-size:11.5px;margin-top:3px}
.footer-art{position:absolute;left:0;bottom:0}
.contact{position:absolute;left:30px;bottom:64px;font-size:11px;line-height:1.7;list-style:none}
.contact li{display:flex;align-items:center;gap:8px}
.footer-brand{position:absolute;right:36px;bottom:48px;flex-direction:column;align-items:flex-end;gap:6px}
.footer-brand .row{display:flex;align-items:center;gap:8px}
.footer-brand .brand-name{font-size:15px}
.website{color:var(--navy);font-size:13px;letter-spacing:.5px}
</style>
</head>
<body>
<article class="newsletter">
  <svg class="header-art" width="622" height="170" viewBox="0 0 622 170">
    <defs>
      <linearGradient id="headerTone" x1="0" x2="1" y1="0" y2="0">
        <stop offset="0" stop-color="#e9dd45"/>
        <stop offset=".6" stop-color="#efe36a"/>
        <stop offset="1" stop-color="#d9d6c8"/>
      </linearGradient>
    </defs>
    <rect width="622" height="150" fill="url(#headerTone)" role="img" aria-label="Fotografía de cabecera en tonos amarillos"/>
    <polygon points="0,26 410,26 470,170 0,170" fill="var(--paper)"/>
    <polygon points="452,96 622,96 622,152 474,152" fill="var(--navy)"/>
    <polygon points="474,152 622,152 622,157 476,157" fill="var(--accent-yellow)"/>
    <rect x="470" y="157" width="152" height="13" fill="var(--paper)"/>
  </svg>

  <div class="brand header-brand">
    <span class="brand-mark"></span>
    <span class="brand-name">Montalbán<br>y Asociados</span>
  </div>

  <div class="issue-date">
    <svg width="20" height="20" viewBox="0 0 20 20"><circle cx="10" cy="10" r="10" fill="var(--accent-yellow)"/><rect x="5" y="6" width="10" height="9" fill="none" stroke="var(--navy)" stroke-width="1.4"/><line x1="5" y1="9" x2="15" y2="9" stroke="var(--navy)" stroke-width="1.4"/></svg>
    <span>Santiago,<br>25 de julio de 2018</span>
  </div>

  <section class="letter">
    <div class="greeting">Estimados,</div>
    <p>Por medio del presente, les damos a conocer el Dictamen Ordinario N° 3826-031, emitido por la Dirección del Trabajo el pasado 20 de julio, relativo a los “beneficios históricos”.</p>
    <p>Estos fueron definidos en su oportunidad por este organismo como “...aquellos beneficios que se han otorgado desde siempre... por parte del empleador.</p>
    <p>A partir de este Dictamen, el cual reconsidera el criterio del anterior Director del Trabajo, los beneficios históricos vuelven a ser patrimonio de la empresa y de los trabajadores que los han recibido, dejando de serlo de la organización sindical y de sus socios beneficiados por el solo hecho de haberse “replicado” en un instrumento colectivo durante una negociación.</p>
    <p>Por último, el Dictamen en comento aclara que si un “beneficio histórico” se incrementa de manera real y efectiva producto de una negociación colectiva, únicamente dicho incremento se entenderá originado en el respectivo instrumento colectivo, y en consecuencia, objeto de una posible extensión en el evento de que ésta se haya acordado durante la negociación.</p>
    <p class="highlight">Para mayor análisis de lo resuelto por la Dirección del Trabajo, se puede revisar el Dictámen en comento haciendo <a href="#">click aquí</a></p>
    <p class="closing">Sin otro particular, saluda atentamente a ustedes,</p>
  </section>

  <div class="signature">
    <div class="portrait" role="img" aria-label="Retrato del abogado firmante"></div>
    <div>
      <div class="sig-name">Montalbán &amp; Asociados</div>
      <div class="sig-mail">
        <svg width="14" height="14" viewBox="0 0 14 14"><circle cx="7" cy="7" r="7" fill="var(--brand-blue)"/><rect x="3.5" y="4.5" width="7" height="5" fill="none" stroke="#fff" stroke-width="1"/><polyline points="3.5,4.5 7,7.5 10.5,4.5" fill="none" stroke="#fff" stroke-width="1"/></svg>
        oficina@montalbanyasociados.cl
      </div>
    </div>
  </div>

  <svg class="footer-art" width="622" height="220" viewBox="0 0 622 220">
    <defs>
      <linearGradient id="footerTone" x1="0" x2="1" y1="0" y2="1">
        <stop offset="0" stop-color="#efe35a"/>
        <stop offset="1" stop-color="#e2d52e"/>
      </linearGradient>
    </defs>
    <polygon points="0,60 622,60 622,215 0,215" fill="var(--panel)"/>
    <polygon points="250,100 622,100 622,215 310,215" fill="url(#footerTone)" role="img" aria-label="Imagen de pie en tonos amarillos"/>
    <rect x="0" y="215" width="622" height="5" fill="var(--brand-blue)"/>
  </svg>

  <ul class="contact">
    <li><svg width="10" height="12" viewBox="0 0 10 12"><path d="M5 0a4 4 0 0 0-4 4c0 3 4 8 4 8s4-5 4-8a4 4 0 0 0-4-4z" fill="var(--navy)"/><circle cx="5" cy="4" r="1.5" fill="#fff"/></svg>Av. Los Olmos 4120, piso 5, Providencia</li>
    <li><svg width="10" height="10" viewBox="0 0 10 10"><rect x="0" y="3" width="10" height="7" rx="1" fill="var(--navy)"/><rect x="2" y="0" width="6" height="3" fill="var(--navy)"/></svg>T +56 2 298761540</li>
    <li><svg width="10" height="8" viewBox="0 0 10 8"><rect width="10" height="8" fill="var(--navy)"/><polyline points="0,0 5,4 10,0" fill="none" stroke="#fff" stroke-width="1"/></svg>E oficina@montalbanyasociados.cl</li>
  </ul>

  <div class="brand footer-brand">
    <div class="row">
      <span class="brand-mark"></span>
      <span class="brand-name">Montalbán<br>y Asociados</span>
    </div>
    <span class="website">www.montalbanyasociados.cl</span>
  </div>
</article>
</body>
</html>
```